Brand new letterhead, business card, email signature etc.

We are a financial company in London, UK. Our website is www.quorvane.com. We're wanting a complete remodel of the company colours, letter head, business cards, email signatures, etc. Looking to keep the same font for the company name. I have upload a colour palette that we want to work with. We're looking for company letterhead for outgoing letters/ correspondence, letterhead for internal documentation, email signatures, e-letters. etc. Ultimately we will redesign the entire website also. It is important that our clients get a strong, secure, warm, trustworthy, solid feeling and first impression.
Updates

Designs look the same

Target Market(s)

Institutional investors, (ultra) high net worth individuals

Industry/Entity Type

Finance, Invesments banking.

Font styles to use
Other font styles liked:
• Current font is "Champagne & Limousines"

Requirements
Must have
• Must use the colours provided on the PDF uploaded to the portal. The purple = main colour. The red = accent colour.
Nice to have
• Nice to use same font as now for the company name "Marlowin". Font is "Champagne & Limousines". Nice to have some reference to the old logo flower, but only subtle.
Should not have
• Do not use the colour red from our website. Use the colours provided on the colour palette PDF that I uploaded in the portal.

```html
<!DOCTYPE html>
<html lang="en">
<head>
<meta charset="utf-8">
<title>Marlowin Business Card</title>
<link rel="stylesheet" href="https://fonts.googleapis.com/css2?family=Josefin+Sans:wght@300&family=Arimo:wght@400;700&display=swap">
<style>
  :root {
    --plum: #22051a;
    --accent: #d8341c;
    --paper: #f7f7f5;
    --ink: #1c1c1c;
    --backdrop: #2b2b2b;
  }
  * { margin: 0; padding: 0; box-sizing: border-box; }
  html, body { width: 1200px; height: 874px; overflow: hidden; background: var(--backdrop); }
  .canvas {
    width: 1200px; height: 874px;
    display: flex; flex-direction: column; align-items: center; justify-content: center; gap: 24px;
  }
  .card { width: 700px; height: 400px; position: relative; overflow: hidden; background: var(--paper); }

  /* Front */
  .card-front { display: flex; align-items: center; justify-content: center; gap: 26px; }
  .brand-square { width: 92px; height: 92px; border: 1.5px solid var(--ink); }
  .brand-name {
    font-family: "Josefin Sans", sans-serif; font-weight: 300;
    font-size: 56px; letter-spacing: 14px; color: var(--ink); padding-top: 8px;
  }

  /* Back */
  .card-back .wave { position: absolute; inset: 0; }
  .decor-bloom {
    position: absolute; left: 70px; top: 40px; width: 220px; height: 210px;
    border-radius: 50%;
    background: radial-gradient(circle, rgba(190,150,180,0.28) 0%, rgba(190,150,180,0.08) 55%, rgba(34,5,26,0) 72%);
  }
  .holder { position: absolute; right: 48px; top: 128px; text-align: right; font-family: "Arimo", sans-serif; }
  .holder-name { color: var(--accent); font-weight: 700; font-size: 27px; }
  .holder-role { color: #fff; font-size: 17px; margin-top: 3px; }
  .contact {
    position: absolute; right: 40px; bottom: 22px; text-align: right;
    font-family: "Arimo", sans-serif; font-size: 16px; line-height: 20px; color: var(--ink);
  }
  .contact .address { margin-bottom: 10px; padding-right: 26px; }
  .contact-line { display: flex; justify-content: flex-end; align-items: center; gap: 10px; }
  .contact-line svg { width: 16px; height: 16px; fill: var(--accent); }
</style>
</head>
<body>
<main class="canvas">
  <section class="card card-front">
    <div class="brand-square"></div>
    <div class="brand-name">MARLOWIN</div>
  </section>

  <section class="card card-back">
    <svg class="wave" viewBox="0 0 700 400" preserveAspectRatio="none">
      <path d="M0,0 H700 V215 C620,205 520,210 400,250 C260,300 120,330 0,262 Z" fill="var(--plum)"/>
      <path d="M0,274 C120,342 260,312 400,262 C520,222 620,217 700,227" fill="none" stroke="var(--accent)" stroke-width="9"/>
      <path d="M30,300 C140,350 270,322 400,280 C520,244 620,236 690,240" fill="none" stroke="var(--plum)" stroke-width="4"/>
    </svg>
    <div class="decor-bloom" role="img" aria-label="Faint line-drawn flower decoration"></div>
    <div class="holder">
      <div class="holder-name">Elliot Harrow</div>
      <div class="holder-role">President</div>
    </div>
    <div class="contact">
      <div class="address">2716 Ashgrove Lane<br>Linden Hill, NY 11043</div>
      <div class="contact-line">(612) 5590-3148
        <svg viewBox="0 0 16 16"><path d="M3.5 1.5l2.5 0 1 3.5-1.8 1.2c.8 1.8 2 3 3.8 3.8l1.2-1.8 3.5 1v2.5c0 .8-.7 1.5-1.5 1.5C6.6 14.2 1.8 9.4 2 3c0-.8.7-1.5 1.5-1.5z"/></svg>
      </div>
      <div class="contact-line">name@QUORVANE.com
        <svg viewBox="0 0 16 16"><path d="M1 3.5h14v9H1z M1.5 4l6.5 5 6.5-5" stroke="#f7f7f5" stroke-width="1"/></svg>
      </div>
      <div class="contact-line">www.QUORVANE.com
        <svg viewBox="0 0 16 16"><circle cx="8" cy="8" r="7"/><path d="M1 8h14M8 1c-3 3.5-3 10.5 0 14M8 1c3 3.5 3 10.5 0 14" stroke="#f7f7f5" stroke-width="1" fill="none"/></svg>
      </div>
    </div>
  </section>
</main>
</body>
</html>
```